Gilded Fern Kiosks- Spotlight Moments begin with your Hair

Current website: https://gildedfernkiosks.example/

Features needed to be added:
- customers are able to leave ratings, comments, reviews and videos
- Discount codes
- Shipping features (option for shipping and local delivery)
- Invoices
- Multiple images per product
- Connect Square for payment provider
- add all the means of payment available to show credit cards/ debit cards/ Apple Pay/ Afterpay , etc
- File Hosting

Below is my Shopify store link I’d like all transactions rerouted to for checkout. The website and simply be promoting and marketing but I’d like all transactions in one place and it offers more ways to pay as well.

https://gilded-fern-kiosks-llc-2.shopfront.example/

"Gilded Fern Kiosks: Beauty & Convenience for Women Who Serve"

Target Audience Description:

Black and Brown Active-Duty Service Members, Dependents, and Female Veterans stationed on military installations who seek premium, inclusive beauty products but face limited access to diverse hair textures and shades in standard base exchanges (PX/BX).

Key Webpage Messaging:

· "We See You. We Serve You." — Acknowledging the specific hair care needs of Black and Brown women (coils, curls, protective styles, braiding hair, and wigs).
· "Mission Ready in Minutes." — Highlighting 24/7 vending access for service women with demanding schedules who cannot rely on off-base beauty supply stores.
· "Veteran-Owned. Service-Connected." — Emphasizing trust and shared military experience (SDVOSB/WOSB credentials).

Visual Elements:

· Images of women of color in uniform transitioning to off-duty glamour.
· Icons representing 24/7 Access, PX-Compatible Pricing, and Veteran Tested.

Call to Action (CTA):

"Request Gilded Fern at Your Base Exchange Today."

One Page for Colleges
One Page Dedicated to Government Cintracts and needs

Target Market(s)

College and Military Campuses

Industry/Entity Type

Beauty

Coding

Coded - Design and coding required

Number of Pages Required

2 page

Colors
FFC000
F8CF3A
FAE287
FDF2CF
FEFAEE

Requirements
Must have
• Please ensure ALL designs are targeting the black young adult market using the BUNDLES not the blunt end braiding hair photos. Please use the Shopify model as a reference. Ensure All government website needs are there, along with the ability for contract officers to obtain the documents
Nice to have
• Female models of different ethnicities with long hair extensions similar to Shopify page

```html
<!DOCTYPE html>
<html lang="en">
<head>
<meta charset="utf-8">
<title>Products for Federal Agencies – Gilded Fern Kiosks</title>
<link rel="stylesheet" href="https://fonts.googleapis.com/css2?family=Gloock&family=Outfit:wght@300;400;500;600&display=swap">
<style>
:root{
  --gold:#FFC000;
  --gold-soft:#F8CF3A;
  --gold-pale:#FAE287;
  --cream:#FDF2CF;
  --ivory:#FEFAEE;
  --ink:#000000;
  --text:#2b2b2b;
  --muted:#555555;
  --brand:#C98A1E;
  --line:#dddddd;
  --white:#ffffff;
}
*{margin:0;padding:0;box-sizing:border-box}
html,body{width:1200px;height:2250px;overflow:hidden}
body{position:relative;background:var(--ivory);font-family:"Outfit",sans-serif;color:var(--text)}
.serif{font-family:"Gloock",serif;font-weight:400}

.topbar{position:absolute;left:0;top:0;width:1200px;height:37px;background:var(--ink);color:var(--white);font-size:11px;display:flex;justify-content:center;align-items:center;gap:26px}

.site-header{position:absolute;left:0;top:37px;width:1200px;height:98px;background:#FEF9EC;display:flex;align-items:center}
.brand{position:absolute;left:112px;top:26px;display:flex;align-items:center;gap:8px}
.brand-mark{width:14px;height:14px;background:var(--brand);border-radius:50%}
.brand-name{font-family:"Outfit",sans-serif;font-weight:600;color:var(--brand);font-size:13px;letter-spacing:1.5px}
.main-nav{position:absolute;left:420px;top:38px;display:flex;align-items:center;gap:21px;font-size:13px;color:var(--text)}
.phone{position:absolute;left:951px;top:29px;display:flex;align-items:center;gap:8px;font-size:13px;font-weight:500}
.phone-icon{width:39px;height:39px;border-radius:50%;background:var(--gold);display:flex;align-items:center;justify-content:center}

.hero{position:absolute;left:0;top:135px;width:1200px;height:337px;background:linear-gradient(90deg,#5b5d66 0%,#6e7079 55%,#75777f 100%)}
.hero-photo{position:absolute;left:838px;top:20px;width:160px;height:317px;border-radius:40px 40px 0 0;background:linear-gradient(180deg,#7a3a1c,#5a2a14)}
.hero h1{position:absolute;left:112px;top:110px;font-size:45px;color:var(--white);line-height:1}
.hero p{position:absolute;left:113px;top:172px;font-size:13px;color:var(--white)}

.gallery-main{position:absolute;left:190px;top:563px;width:413px;height:281px;background:radial-gradient(ellipse at 50% 40%,#9a4b22 0%,#7a3818 45%,#a7a9b5 80%)}
.thumbs{position:absolute;left:190px;top:851px;display:flex;gap:16px}
.thumb{width:91px;height:85px;background:linear-gradient(90deg,#a5a7b2 30%,#7a3a1c 45%,#7a3a1c 58%,#a5a7b2 72%)}
.thumb.light{background:linear-gradient(90deg,#a5a7b2 30%,#d9a85a 45%,#d9a85a 58%,#a5a7b2 72%)}

.product-copy{position:absolute;left:653px;top:600px;width:370px}
.product-copy h2{font-size:41px;color:var(--ink);line-height:1}
.product-copy .lede{margin-top:18px;font-size:13px;color:var(--muted)}
.product-copy ul{list-style:none;margin-top:13px;font-size:13px;color:var(--muted);line-height:21px}
.product-copy h2.second{margin-top:18px}
.product-copy .overview{margin-top:16px;font-size:13px;color:var(--muted);line-height:19px}

.section-title{position:absolute;left:0;width:1200px;text-align:center;font-size:45px;color:var(--ink)}
.reg-table{position:absolute;left:162px;top:1101px;width:877px;height:216px;background:var(--white);box-shadow:0 4px 18px rgba(0,0,0,.06);display:grid;grid-template-columns:repeat(4,1fr)}
.reg-col{border-right:1px solid var(--line);text-align:center}
.reg-col:last-child{border-right:none}
.reg-col h3{height:56px;border-bottom:1px solid var(--line);display:flex;align-items:center;justify-content:center;font-family:"Gloock",serif;font-weight:400;font-size:24px;color:var(--ink)}
.reg-col ul{list-style:none;padding-top:22px;font-size:13.5px;color:var(--muted);line-height:37.5px}

.info-card{position:absolute;top:1414px;width:411px;height:282px;background:var(--white);box-shadow:0 4px 18px rgba(0,0,0,.06)}
.info-card h3{height:56px;display:flex;align-items:center;justify-content:center;font-family:"Gloock",serif;font-weight:400;font-size:24px}
.info-card.specs{left:175px}
.info-card.specs h3{background:var(--gold);color:var(--ink)}
.info-card.medical{left:614px}
.info-card.medical h3{background:var(--ink);color:var(--white)}
.info-card ul{list-style:none;text-align:center;padding-top:17px;font-size:13px;color:var(--text);line-height:37.5px}

.cta{position:absolute;left:489px;top:1734px;width:222px;height:47px;border-radius:24px;background:var(--gold);display:flex;align-items:center;justify-content:center;font-size:12px;font-weight:500;color:var(--ink)}

.site-footer{position:absolute;left:0;top:1858px;width:1200px;height:392px;background:var(--ink);color:var(--white)}
.footer-brand{position:absolute;left:0;top:128px;width:1200px;display:flex;justify-content:center;align-items:center;gap:10px}
.footer-brand .brand-mark{width:18px;height:18px}
.footer-brand .brand-name{font-size:17px;letter-spacing:2.5px}
.footer-nav{position:absolute;left:191px;top:199px;display:flex;gap:48px;font-size:13px}
.socials{position:absolute;left:0;top:2113px;margin-top:-1858px;width:1200px;display:flex;justify-content:center;gap:8px}
.social{width:45px;height:45px;border-radius:50%;background:#2a2a2a}
.social.active{background:var(--gold)}
.footer-rule{position:absolute;left:112px;top:346px;width:976px;height:1px;background:#333}
.copyright{position:absolute;left:0;top:360px;width:1200px;text-align:center;font-size:12px}
</style>
</head>
<body>

<div class="topbar">
  <span>Government &amp; Federal Contracting Partner</span>
  <span>|</span>
  <span>SBA-Certified SDVOSB | WOSB | Maryland MBE</span>
</div>

<header class="site-header">
  <div class="brand"><span class="brand-mark"></span><span class="brand-name">GILDED FERN KIOSKS LLC</span></div>
  <nav class="main-nav">
    <svg width="16" height="15" viewBox="0 0 16 15" aria-hidden="true"><path d="M8 0L0 7h2v8h4v-5h4v5h4V7h2z" fill="#FFC000"/></svg>
    <span>Shop Hair</span><span>Shop Fernline</span><span>Government Contracts</span><span>Student Spotlight</span><span>About</span>
  </nav>
  <div class="phone">
    <span class="phone-icon"><svg width="16" height="16" viewBox="0 0 24 24" aria-hidden="true"><path d="M6.6 10.8a15.1 15.1 0 0 0 6.6 6.6l2.2-2.2c.3-.3.7-.4 1-.2 1.1.4 2.3.6 3.6.6.6 0 1 .4 1 1V20c0 .6-.4 1-1 1A17 17 0 0 1 3 4c0-.6.4-1 1-1h3.5c.6 0 1 .4 1 1 0 1.3.2 2.5.6 3.6.1.3 0 .7-.2 1z" fill="#000"/></svg></span>
    <span>(555) 014-2287</span>
  </div>
</header>

<section class="hero">
  <div class="hero-photo" role="img" aria-label="Hand holding a long reddish-brown deep wave hair bundle"></div>
  <h1 class="serif">Products for Federal Agencies</h1>
  <p>Medical-Grade Human Hair &amp; Overseas Hygiene Kits</p>
</section>

<div class="gallery-main" role="img" aria-label="Close-up of reddish-brown deep wave human hair bundle"></div>
<div class="thumbs">
  <div class="thumb" role="img" aria-label="Copper deep wave bundle held up"></div>
  <div class="thumb" role="img" aria-label="Auburn deep wave bundle held up"></div>
  <div class="thumb" role="img" aria-label="Dark brown deep wave bundle held up"></div>
  <div class="thumb light" role="img" aria-label="Honey blonde deep wave bundle held up"></div>
</div>

<div class="product-copy">
  <h2 class="serif">Product Category 1</h2>
  <p class="lede">Human Hair for Medical Wigs &amp; Toupees</p>
  <ul><li>For: VA Hospitals.</li><li>Cancer Treatment Centers.</li><li>Military Medical Facilities.</li></ul>
  <h2 class="serif second">Product Overview</h2>
  <p class="overview">We Supply 100% Remy Human Hair Specifically Selected for Medical Wig and Toupee Construction. Ethically Sourced, Cuticle-aligned, Hypoallergenic, and Suitable for Sensitive Scalps.</p>
</div>

<h2 class="section-title serif" style="top:1022px">Registration Status</h2>
<div class="reg-table">
  <div class="reg-col"><h3>Product Type</h3><ul><li>Human Hair Bundles</li><li>Closures</li><li>Frontals</li></ul></div>
  <div class="reg-col"><h3>Texture</h3><ul><li>Straight</li><li>Body Wave / Deep Wave</li><li>All Textures</li></ul></div>
  <div class="reg-col"><h3>Lengths</h3><ul><li>12"–30"</li><li>Standard</li><li>13x4, 13x6</li></ul></div>
  <div class="reg-col"><h3>Quantity</h3><ul><li>207 Units</li><li>4 Units</li><li>7 Units</li></ul></div>
</div>

<div class="info-card specs">
  <h3>Product Specifications</h3>
  <ul><li>100% Remy Human Hair</li><li>Ethically sourced Brazilian/Indian hair</li><li>Sterilized &amp; hypoallergenic</li><li>Batch-tested quality assurance</li><li>FDA-aligned cosmetic compliance</li></ul>
</div>
<div class="info-card medical">
  <h3>Medical Applications</h3>
  <ul><li>Medical Applications</li><li>Cancer patient cranial prostheses</li><li>Alopecia medical wigs</li><li>Veteran scalp injury toupees</li><li>Burn victim hair systems</li></ul>
</div>

<div class="cta">Request Product Spec Sheet</div>

<footer class="site-footer">
  <div class="footer-brand"><span class="brand-mark"></span><span class="brand-name">GILDED FERN KIOSKS LLC</span></div>
  <nav class="footer-nav"><span>Home</span><span>Shop Hair</span><span>Shop Fernline</span><span>Government Contracts</span><span>Student Spotlight</span><span>About Us</span><span>Contact Us</span></nav>
  <div class="socials" style="top:255px;margin-top:0">
    <span class="social active"></span><span class="social"></span><span class="social"></span><span class="social"></span>
  </div>
  <div class="footer-rule"></div>
  <p class="copyright">©Copyright 2025. Gilded Fern Kiosks LLC .All Rights Reserved.</p>
</footer>

</body>
</html>
```